Boom Way Hoist Service Business Cards

I need a business card for "Boom Way Hoist and Haulage"

Boomway2023@hoistmail.net

Hoist Works LLC, Boom Way Hoist and Haulage LLC

555.014.7260 | www.BOOMWAYHOISTS.example

Central Westmark & Northeast Eastmere

(IN) 14820 Maple Lane Fernvale, WM 46000

(OH) 2450 Pell Street Ashford, Eastmere 44300

Colors
0094D4
00A9DD
6FCCEA
C7EBF8
E9F6FB
59FF00
82FF00
B8FF75
E3FFCB
F4FFEA
EE7325
F08F49
F5BC92
FAE3D3
FDF4ED
EB3D1F
EC4F4E
F09395
F8D3D4
FCEDEE
E54698
E96AAD
F1A4CE
F9D9EA
FCEFF6
A7469A
B969AE
D3A5CF
EDDBEB
F8F0F9

```html
<!DOCTYPE html>
<html lang="en">
<head>
<meta charset="utf-8">
<title>Boom Way Hoist and Haulage – Business Cards</title>
<link rel="stylesheet" href="https://fonts.googleapis.com/css2?family=Montserrat:wght@400;500;600;700;800&display=swap">
<style>
  :root {
    --bg: #a3a4a9;
    --card: #141414;
    --white: #ffffff;
    --green: #4cbb3f;
    --red: #e8452c;
    --grey-text: #cfcfcf;
    --art-dark: #2b2b2b;
    --art-mid: #5a5a5a;
  }
  * { box-sizing: border-box; margin: 0; padding: 0; }
  html, body { width: 1200px; height: 876px; overflow: hidden; }
  body {
    background: radial-gradient(ellipse at 50% 30%, #b6b7bc 0%, var(--bg) 70%);
    font-family: "Montserrat", sans-serif;
    position: relative;
  }
  .card {
    position: absolute;
    top: 148px;
    width: 340px;
    height: 580px;
    background: var(--card);
    border-radius: 4px;
    box-shadow: 0 18px 40px rgba(0,0,0,.35);
    overflow: hidden;
    color: var(--white);
  }
  /* Front */
  .card-front { left: 220px; }
  .front-brand { position: absolute; left: 34px; top: 38px; right: 30px; }
  .brand-name {
    font-weight: 800; font-size: 62px; line-height: .92; letter-spacing: 1px;
    color: var(--white); text-transform: uppercase;
  }
  .brand-sub {
    margin-top: 12px; font-weight: 700; font-size: 12px; letter-spacing: 1.5px;
    line-height: 1.3; text-transform: uppercase; color: var(--white);
  }
  .front-art {
    position: absolute; left: 24px; right: 24px; top: 250px; bottom: 28px;
    border-radius: 3px;
    background: linear-gradient(160deg, var(--art-mid) 0%, var(--art-dark) 45%, #3a4a35 75%, #5a2a20 100%);
  }
  /* Back */
  .card-back { left: 640px; padding: 40px 32px; }
  .back-brand { display: flex; align-items: center; gap: 10px; }
  .brand-dot { width: 14px; height: 14px; border-radius: 50%; background: var(--green); flex: none; }
  .back-brand .brand-name { font-size: 30px; line-height: 1; letter-spacing: .5px; }
  .person { margin-top: 70px; }
  .person-name { font-weight: 700; font-size: 26px; line-height: 1.1; }
  .person-name .first { color: var(--red); display: block; }
  .person-name .last { color: var(--green); display: block; }
  .person-role { font-size: 13px; color: var(--grey-text); margin-top: 4px; letter-spacing: 1px; }
  .contact-list { list-style: none; margin-top: 18px; }
  .contact-list li { display: flex; align-items: center; gap: 8px; font-size: 13px; margin-bottom: 7px; font-weight: 500; white-space: nowrap; }
  .contact-list svg { width: 14px; height: 14px; flex: none; }
  .offices { margin-top: 30px; }
  .office { margin-bottom: 22px; }
  .office-title { font-weight: 700; font-size: 18px; color: var(--green); }
  .office-address { font-size: 14px; line-height: 1.45; font-weight: 500; margin-top: 3px; }
</style>
</head>
<body>
  <section class="card card-front">
    <div class="front-brand">
      <div class="brand-name">Boom<br>Way</div>
      <div class="brand-sub">Hoist<br>&amp; Haulage<br>Services</div>
    </div>
    <div class="front-art" role="img" aria-label="Illustration of a red boom truck and a green mobile crane in front of a grey construction skyline"></div>
  </section>

  <section class="card card-back">
    <div class="back-brand">
      <span class="brand-dot"></span>
      <span class="brand-name">Boom Way</span>
    </div>
    <div class="person">
      <div class="person-name"><span class="first">Darren</span><span class="last">Whitlock</span></div>
      <div class="person-role">Owner</div>
      <ul class="contact-list">
        <li><svg viewBox="0 0 16 16"><path fill="#e8452c" d="M3 1l3 3-1.5 2c1 2 3 4 5.5 5.5L12 10l3 3-2 2C7 15 1 9 1 3z"/></svg>555.014.7260</li>
        <li><svg viewBox="0 0 16 16"><rect x="1" y="3" width="14" height="10" fill="#e8452c"/><path d="M1 3l7 6 7-6" stroke="#141414" stroke-width="1.5" fill="none"/></svg>Boomway2023@hoistmail.net</li>
        <li><svg viewBox="0 0 16 16"><circle cx="8" cy="8" r="6.5" fill="none" stroke="#e8452c" stroke-width="1.5"/><path d="M1.5 8h13M8 1.5c-3 3.5-3 9.5 0 13M8 1.5c3 3.5 3 9.5 0 13" stroke="#e8452c" stroke-width="1.2" fill="none"/></svg>www.BOOMWAYHOISTS.example</li>
      </ul>
    </div>
    <div class="offices">
      <div class="office">
        <div class="office-title">Central Westmark</div>
        <div class="office-address">14820 Maple Lane Fernvale,<br>WM 46000</div>
      </div>
      <div class="office">
        <div class="office-title">Northeast Eastmere</div>
        <div class="office-address">2450 Pell Street Ashford<br>Eastmere 44300</div>
      </div>
    </div>
  </section>
</body>
</html>
```